Pelican Litigation Funding Letterhead & Document Template

We need a letter head designed for our fund. Our fund works with law firms and investors across the globe. We need a a cover letter template as well as a document template for subsequent pages. Blue and white color scheme is preferred. This is our predecessor's website: https://www.pelicanvq.com/index.html. Please see our logo attached. The logo color code is #19478d. Font is Gotham-Medium.
Target Market(s)
Sophisticated investors and law firms
Font styles to use
Sans Serif
Colors
0255a3

```html
<!DOCTYPE html>
<html lang="en">
<head>
<meta charset="utf-8">
<title>Pelican Litigation Funding Letterhead</title>
<link rel="stylesheet" href="https://fonts.googleapis.com/css2?family=Montserrat:wght@500;600&family=Inter:wght@400&display=swap">
<style>
  :root {
    --brand-blue: #1a4a8e;
    --brand-navy: #0b2561;
    --paper: #ffffff;
    --ink: #1b1b1b;
    --backdrop: #eceef2;
  }
  html, body {
    margin: 0;
    width: 1200px;
    height: 1200px;
    overflow: hidden;
    background: var(--backdrop);
  }
  .letterhead {
    position: absolute;
    left: 200px;
    top: 34px;
    width: 800px;
    height: 1131px;
    background: var(--paper);
    box-shadow: 0 6px 24px rgba(0,0,0,0.12);
    overflow: hidden;
  }
  .header-band {
    position: absolute;
    left: 0; top: 0;
    width: 800px; height: 121px;
    background: var(--brand-blue);
  }
  .brand-tab {
    position: absolute;
    left: 21px; top: 96px;
    width: 259px; height: 48px;
    background: var(--paper);
    display: flex;
    align-items: center;
    justify-content: center;
    font-family: "Montserrat", sans-serif;
    font-weight: 500;
    font-size: 15.5px;
    letter-spacing: 0.4px;
    color: var(--brand-blue);
    text-transform: uppercase;
  }
  .tel-tab {
    position: absolute;
    left: 554px; top: 94px;
    width: 246px; height: 27px;
    background: var(--brand-navy);
    border-radius: 14px 0 0 0;
    font-family: "Montserrat", sans-serif;
    font-weight: 500;
    font-size: 15px;
    color: var(--paper);
    line-height: 27px;
    text-align: right;
    padding-right: 55px;
    box-sizing: border-box;
  }
  .letter-title {
    position: absolute;
    left: 60px; top: 198px;
    margin: 0;
    font-family: "Montserrat", sans-serif;
    font-weight: 600;
    font-size: 24px;
    letter-spacing: 0.5px;
    color: var(--brand-navy);
  }
  .letter-body {
    position: absolute;
    left: 60px; top: 246px;
    width: 680px;
    font-family: "Inter", sans-serif;
    font-size: 14.6px;
    line-height: 19.3px;
    color: var(--ink);
    text-align: justify;
  }
  .letter-body p { margin: 0 0 19.3px; }
  .letter-body p.tight { margin-bottom: 0; }
  .signature {
    position: absolute;
    left: 559px; top: 996px;
    width: 162px;
    border-top: 1px solid var(--brand-blue);
    text-align: center;
    padding-top: 9px;
    font-family: "Montserrat", sans-serif;
    font-weight: 500;
    font-size: 10.5px;
    color: var(--brand-navy);
  }
  .footer-rule {
    position: absolute;
    left: 42px; top: 1048px;
    width: 716px;
    border-top: 1.5px solid var(--brand-blue);
  }
  .address {
    position: absolute;
    left: 55px; top: 1056px;
    display: flex;
    align-items: center;
    gap: 5px;
    font-family: "Montserrat", sans-serif;
    font-weight: 500;
    font-size: 16.5px;
    color: var(--ink);
  }
  .footer-band {
    position: absolute;
    left: 0; top: 1089px;
    width: 800px; height: 42px;
    background: var(--brand-blue);
    font-family: "Montserrat", sans-serif;
    font-weight: 500;
    font-size: 14.5px;
    color: var(--paper);
  }
  .footer-band svg { position: absolute; left: 0; top: 0; }
  .footer-fax { position: absolute; left: 54px; top: 11px; }
  .footer-email { position: absolute; right: 55px; top: 11px; }
</style>
</head>
<body>
  <main class="letterhead">
    <div class="header-band"></div>
    <div class="brand-tab">Pelican Litigation Funding</div>
    <div class="tel-tab">Tel: (555) 014-7200</div>

    <h1 class="letter-title">YOUR TEXT HERE</h1>

    <section class="letter-body">
      <p>Lorem ipsum, or lipsum as it is sometimes known, is dummy text used in laying out print, graphic or web designs. The passage is attributed to an unknown typesetter in the 15th century who is thought to have scrambled parts of Cicero's De Finibus Bonorum et Malorum for use in a type specimen book. It usually begins with:</p>
      <p class="tight">“Lorem ipsum dolor sit amet, consectetur adipiscing elit, sed do eiusmod tempor incididunt ut labore et dolore magna aliqua.”</p>
      <p>The purpose of lorem ipsum is to create a natural looking block of text (sentence, paragraph, page, etc.) that doesn't distract from the layout. A practice not without controversy, laying out pages with meaningless filler text can be very useful when the focus is meant to be on design, not content.</p>
      <p>The passage experienced a surge in popularity during the 1960s when Letraset used it on their dry-transfer sheets, and again during the 90s as desktop publishers bundled the text with their software. Today it's seen all around the web; on templates, websites, and stock designs. Use our generator to get your own, or read on for the authoritative history of lorem ipsum.</p>
      <p>Lorem ipsum, or lipsum as it is sometimes known, is dummy text used in laying out print, graphic or web designs. The passage is attributed to an unknown typesetter in the 15th century who is thought to have scrambled parts of Cicero's De Finibus Bonorum et Malorum for use in a type specimen book. It usually begins with:</p>
      <p class="tight">“Lorem ipsum dolor sit amet, consectetur adipiscing elit, sed do eiusmod tempor incididunt ut labore et dolore magna aliqua.”</p>
      <p>The purpose of lorem ipsum is to create a natural looking block of text (sentence, paragraph, page, etc.) that doesn't distract from the layout. A practice not without controversy, laying out pages with meaningless filler text can be very useful when the focus is meant to be on design, not content.</p>
      <p>The passage experienced a surge in popularity during the 1960s when Letraset used it on their dry-transfer sheets, and again during the 90s as desktop publishers bundled the text with their software. Today it's seen all around the web; on templates, websites, and stock designs. Use our generator to get your own, or read on for the authoritative history of lorem ipsum.</p>
    </section>

    <div class="signature">Signature Authority</div>

    <div class="footer-rule"></div>
    <div class="address">
      <svg width="16" height="16" viewBox="0 0 16 16" aria-hidden="true">
        <circle cx="8" cy="8" r="8" fill="var(--brand-blue)"/>
        <path d="M8 3.6a2.6 2.6 0 0 0-2.6 2.6c0 1.9 2.6 5.2 2.6 5.2s2.6-3.3 2.6-5.2A2.6 2.6 0 0 0 8 3.6z" fill="#fff"/>
        <circle cx="8" cy="6.2" r="0.9" fill="var(--brand-blue)"/>
      </svg>
      <span>: Penthouse Floor 480 Harbor Avenue, Suite 1200 Bayport, Texas 70000</span>
    </div>

    <footer class="footer-band">
      <svg width="800" height="42" viewBox="0 0 800 42" aria-hidden="true">
        <polygon points="369,0 434,0 460,42 344,42" fill="var(--brand-navy)"/>
      </svg>
      <span class="footer-fax">Fax: (555) 014-7300</span>
      <span class="footer-email">Email: info@pelicanvq.com</span>
    </footer>
  </main>
</body>
</html>
```